Solar energy proposal for homeowners

I am providing households with solar energy proposals, and I need a high-quality brochure that is packaged cleverly to attract the homeowner's attention. Take a look at the one page solar brochure that I have included to get an idea of text and content.

Target Market(s)

Residential Homeowners

Industry/Entity Type

Solar

Requirements
Must have
• High quality document

```html
<!DOCTYPE html>
<html lang="en">
<head>
<meta charset="utf-8">
<title>Brightvale Energy – Solar Flyer</title>
<link href="https://fonts.googleapis.com/css2?family=Montserrat:wght@300;400;500;600;700;800&display=swap" rel="stylesheet">
<style>
  :root {
    --blue: #0a9fd8;
    --cyan: #00b6cc;
    --teal: #2bb3c0;
    --green: #9ccc3c;
    --lime: #b3d334;
    --navy: #253a6e;
    --ink: #1c1c1c;
    --paper: #f3f3f4;
    --white: #ffffff;
    --backdrop: #e4e4e2;
  }
  * { box-sizing: border-box; margin: 0; padding: 0; }
  html, body { width: 1200px; height: 1117px; overflow: hidden; }
  body { background: var(--backdrop); font-family: "Montserrat", sans-serif; position: relative; }

  .flyer {
    position: absolute; left: 204px; top: 0;
    width: 1059px; height: 1495px;
    transform: scale(0.7472); transform-origin: top left;
    background: var(--paper); overflow: hidden;
  }
  .flyer > * { position: absolute; }

  .top-white { left: 0; top: 0; width: 1059px; height: 186px; background: var(--white); }
  .hero-shapes { left: 0; top: 0; }

  .brand { left: 95px; top: 82px; display: flex; align-items: center; gap: 14px; white-space: nowrap;
    font-family: "Montserrat", sans-serif; font-weight: 500; font-size: 37px; color: var(--teal); letter-spacing: -0.5px; }
  .brand-mark { width: 34px; height: 34px; background: var(--teal); flex: none; }

  .headline { left: 97px; top: 222px; color: var(--white); }
  .headline .lead { font-weight: 500; font-size: 48px; line-height: 56px; letter-spacing: -0.5px; }
  .headline .punch { font-weight: 800; font-size: 55px; line-height: 56px; letter-spacing: -0.5px; }
  .tagline { left: 96px; top: 462px; color: var(--white); font-weight: 400; font-size: 33px; line-height: 36px; }

  .tag { height: 46px; display: flex; align-items: center; justify-content: center;
    color: var(--white); font-weight: 800; font-size: 29px; letter-spacing: -0.3px;
    background: linear-gradient(90deg, var(--blue), var(--teal) 55%, var(--green));
    clip-path: polygon(4% 0, 100% 0, 96% 100%, 0 100%); }
  .tag-about { left: 95px; top: 630px; width: 370px; }
  .tag-why { left: 580px; top: 630px; width: 368px; }
  .tag-service { left: 345px; top: 917px; width: 368px; z-index: 2; }

  .about-text { left: 95px; top: 688px; width: 410px; font-size: 19.5px; line-height: 25.5px; color: var(--ink); font-weight: 400; letter-spacing: -0.2px; }
  .divider { left: 529px; top: 630px; width: 1.5px; height: 236px; background: var(--navy); opacity: .7; }

  .benefits { left: 580px; top: 686px; list-style: none; }
  .benefits li { display: flex; align-items: center; gap: 16px; font-size: 20.5px; height: 34px; color: var(--ink); letter-spacing: -0.2px; }
  .benefits svg { flex: none; }

  .navy-band { left: 0; top: 1120px; width: 1059px; height: 255px; background: var(--navy); }
  .service-card { left: 83px; top: 938px; width: 894px; height: 365px; background: var(--white); box-shadow: 0 2px 6px rgba(0,0,0,.08); }

  .service { width: 430px; display: flex; gap: 24px; }
  .service-1 { left: 122px; top: 1008px; }
  .service-2 { left: 548px; top: 1008px; }
  .service-3 { left: 122px; top: 1148px; }
  .service-4 { left: 548px; top: 1148px; }
  .service svg { flex: none; margin-top: 0; }
  .service h3 { font-size: 22.5px; font-weight: 700; color: var(--navy); margin-top: 3px; letter-spacing: -0.3px; }
  .service p { font-size: 19.5px; line-height: 23px; color: var(--ink); margin-top: 6px; letter-spacing: -0.2px; }

  .footer-white { left: 0; top: 1360px; width: 1059px; height: 135px; background: var(--white);
    clip-path: polygon(61.5% 0, 100% 0, 100% 100%, 0 100%, 0 0); }
  .phone-bar { left: 0; top: 1372px; width: 652px; height: 103px;
    background: radial-gradient(ellipse at 45% 0%, #4cc3ec 0%, var(--blue) 40%, #0396d2 100%);
    clip-path: polygon(0 0, 100% 0, 92.5% 100%, 0 100%);
    display: flex; align-items: center; gap: 14px; padding-left: 92px;
    color: var(--white); font-weight: 700; font-size: 57px; letter-spacing: -0.5px; }
  .contact { left: 670px; top: 1390px; list-style: none; }
  .contact li { display: flex; align-items: center; gap: 10px; font-weight: 700; font-size: 20.5px; color: var(--ink); height: 33px; }
</style>
</head>
<body>
<main class="flyer">
  <div class="top-white"></div>

  <svg class="hero-shapes" width="1059" height="600" viewBox="0 0 1059 600">
    <defs>
      <linearGradient id="heroBlue" x1="0" y1="0" x2="1" y2="0.3">
        <stop offset="0" stop-color="#0a9bd8"/>
        <stop offset="1" stop-color="#00bccb"/>
      </linearGradient>
      <linearGradient id="frameGreen" x1="0" y1="0" x2="1" y2="1">
        <stop offset="0" stop-color="#b3d334"/>
        <stop offset="0.55" stop-color="#8fcc63"/>
        <stop offset="1" stop-color="#0fb6cf"/>
      </linearGradient>
      <linearGradient id="photoTone" x1="0" y1="0" x2="0" y2="1">
        <stop offset="0" stop-color="#7b8a86"/>
        <stop offset="0.45" stop-color="#3b3f4c"/>
        <stop offset="0.7" stop-color="#c9ccd0"/>
        <stop offset="1" stop-color="#4f7f34"/>
      </linearGradient>
    </defs>
    <polygon points="0,186 527,186 472,290 545,430 480,575 0,575" fill="url(#heroBlue)"/>
    <polygon points="628,25 665,25 518,290 642,540 1059,540 1059,575 610,575 475,290" fill="url(#frameGreen)"/>
    <polygon points="648,25 1059,25 1059,540 642,540 520,290" fill="url(#photoTone)" role="img" aria-label="Aerial photo of a white family home with solar panels on its dark roof, surrounded by neighbouring houses and green trees"/>
  </svg>

  <div class="brand"><span class="brand-mark"></span>Brightvale Energy</div>

  <h1 class="headline">
    <div class="lead">SOLAR FOR $0</div>
    <div class="punch">DOWN.</div>
    <div class="punch">NO LIENS.</div>
    <div class="punch">NO KIDDING.</div>
  </h1>
  <p class="tagline">Power Your Future with<br>Brightvale Energy</p>

  <h2 class="tag tag-about">ABOUT US</h2>
  <p class="about-text">At Brightvale Energy, our mission is to make solar simple and accessible for everyone. No high-pressure sales-just the information you need to make a smart choice. With our solar rental program, you can lower your monthly energy costs and pay less than your current electricity bill.</p>
  <div class="divider"></div>

  <h2 class="tag tag-why">WHY CHOOSE US?</h2>
  <ul class="benefits">
    <li><svg width="16" height="16" viewBox="0 0 16 16"><circle cx="8" cy="8" r="8" fill="#0a9fd8"/><path d="M4.5 8.2l2.3 2.3 4.6-4.8" stroke="#fff" stroke-width="2" fill="none"/></svg>No financing</li>
    <li><svg width="16" height="16" viewBox="0 0 16 16"><circle cx="8" cy="8" r="8" fill="#0a9fd8"/><path d="M4.5 8.2l2.3 2.3 4.6-4.8" stroke="#fff" stroke-width="2" fill="none"/></svg>No liensNo down payment</li>
    <li><svg width="16" height="16" viewBox="0 0 16 16"><circle cx="8" cy="8" r="8" fill="#0a9fd8"/><path d="M4.5 8.2l2.3 2.3 4.6-4.8" stroke="#fff" stroke-width="2" fill="none"/></svg>No insurance costs</li>
    <li><svg width="16" height="16" viewBox="0 0 16 16"><circle cx="8" cy="8" r="8" fill="#0a9fd8"/><path d="M4.5 8.2l2.3 2.3 4.6-4.8" stroke="#fff" stroke-width="2" fill="none"/></svg>No long-term commitment</li>
    <li><svg width="16" height="16" viewBox="0 0 16 16"><circle cx="8" cy="8" r="8" fill="#0a9fd8"/><path d="M4.5 8.2l2.3 2.3 4.6-4.8" stroke="#fff" stroke-width="2" fill="none"/></svg>No maintenance costs</li>
  </ul>

  <div class="navy-band"></div>
  <div class="service-card"></div>
  <h2 class="tag tag-service">OUR BEST SERVICE</h2>

  <div class="service service-1">
    <svg width="84" height="94" viewBox="0 0 84 94"><polygon points="42,2 82,24 82,70 42,92 2,70 2,24" fill="#2bb3c0"/><polygon points="42,10 75,28 75,66 42,84 9,66 9,28" fill="#253a6e"/><circle cx="42" cy="40" r="12" fill="none" stroke="#fff" stroke-width="3"/><text x="42" y="46" text-anchor="middle" font-family="Montserrat, sans-serif" font-weight="800" font-size="16" fill="#fff">$</text><path d="M34 54v12l8-5 8 5V54" fill="#fff"/></svg>
    <div><h3>Affordable &amp; Transparent</h3><p>Simple pricing, no hidden fees and a fixed monthly rate lower than typical energy bills.</p></div>
  </div>
  <div class="service service-2">
    <svg width="84" height="94" viewBox="0 0 84 94"><polygon points="42,2 82,24 82,70 42,92 2,70 2,24" fill="#2bb3c0"/><polygon points="42,10 75,28 75,66 42,84 9,66 9,28" fill="#253a6e"/><circle cx="42" cy="47" r="15" fill="none" stroke="#fff" stroke-width="6" stroke-dasharray="6 4"/><circle cx="42" cy="47" r="7" fill="none" stroke="#fff" stroke-width="3"/></svg>
    <div><h3>Expert Installation</h3><p>Certified professionals handle installation, maintenance, and repairs end to end.</p></div>
  </div>
  <div class="service service-3">
    <svg width="84" height="94" viewBox="0 0 84 94"><polygon points="42,2 82,24 82,70 42,92 2,70 2,24" fill="#2bb3c0"/><polygon points="42,10 75,28 75,66 42,84 9,66 9,28" fill="#253a6e"/><circle cx="42" cy="46" r="11" fill="none" stroke="#fff" stroke-width="3"/><circle cx="42" cy="44" r="3.5" fill="#fff"/><path d="M35 56l-3 12 6-3 4 5 4-5 6 3-3-12" fill="#fff"/><circle cx="30" cy="30" r="2" fill="#fff"/><circle cx="42" cy="26" r="2" fill="#fff"/><circle cx="54" cy="30" r="2" fill="#fff"/></svg>
    <div><h3>Local Expertise</h3><p>Florida-based team that understands the<br>needs of Orlando and statewide homeowners.</p></div>
  </div>
  <div class="service service-4">
    <svg width="84" height="94" viewBox="0 0 84 94"><polygon points="42,2 82,24 82,70 42,92 2,70 2,24" fill="#2bb3c0"/><polygon points="42,10 75,28 75,66 42,84 9,66 9,28" fill="#253a6e"/><path d="M42 50c-10 0-14-8-14-16 10 0 14 6 14 16zM42 50c0-10 5-16 14-16 0 8-4 16-14 16z" fill="#fff"/><path d="M24 58c6 0 10 4 18 4s12-4 18-6v6c-6 4-12 8-20 8s-12-4-16-4z" fill="#fff"/></svg>
    <div><h3>Eco-Friendly</h3><p>Clean, renewable solar energy that helps reduce your carbon footprint.</p></div>
  </div>

  <div class="footer-white"></div>
  <div class="phone-bar">
    <svg width="46" height="58" viewBox="0 0 46 58"><path d="M8 2l10 0 5 14-7 6c3 8 8 15 15 20l7-6 8 8-5 10c-2 2-6 3-10 1C17 45 6 30 2 12 1 7 4 3 8 2z" fill="#fff"/></svg>
    (407)555-0142
  </div>
  <ul class="contact">
    <li><svg width="18" height="22" viewBox="0 0 18 22"><path d="M9 1a8 8 0 0 1 8 8c0 6-8 12-8 12S1 15 1 9a8 8 0 0 1 8-8z" fill="#0a9fd8"/><circle cx="9" cy="9" r="3" fill="#fff"/></svg>123 Anywhere St., Any City</li>
    <li><svg width="20" height="20" viewBox="0 0 20 20"><circle cx="10" cy="10" r="9" fill="#0a9fd8"/><ellipse cx="10" cy="10" rx="4" ry="8" fill="none" stroke="#fff" stroke-width="1.2"/><path d="M2 10h16M3.5 6h13M3.5 14h13" stroke="#fff" stroke-width="1.2"/></svg>www.brightvaleenergy.com</li>
  </ul>
</main>
</body>
</html>
```